Need business card design
Velin Medical
Simple
Tobias Morvel
CEO
12345 any street
city, state 98765
tmorvel@velinmedical.net
www.velinmedical.net
Just looking for design for now. Additional info will be added later

```html
<!DOCTYPE html>
<html lang="en">
<head>
<meta charset="utf-8">
<title>Velin Medical – Business Card</title>
<link href="https://fonts.googleapis.com/css2?family=Arimo:wght@400;700&display=swap" rel="stylesheet">
<style>
  :root {
    --stage: #d3d3d3;
    --stage-edge: #c4c4c4;
    --navy: #3e5068;
    --green: #2fa83a;
    --white: #ffffff;
    --ink: #3e5068;
  }
  * { margin: 0; padding: 0; box-sizing: border-box; }
  html, body {
    width: 1200px; height: 883px; overflow: hidden;
    background: var(--stage);
    font-family: "Arimo", Arial, sans-serif;
  }
  .stage {
    position: relative; width: 1200px; height: 883px;
    border: 10px solid var(--stage-edge);
  }
  .card {
    position: absolute; left: 331px; width: 581px; height: 329px;
    overflow: hidden;
  }
  .card--front { top: 67px; background: var(--navy); }
  .card--back { top: 487px; background: var(--white); }

  .brand {
    position: absolute; display: flex; align-items: center; gap: 14px;
    font-weight: 700; white-space: nowrap; line-height: 1;
  }
  .brand__mark { background: var(--green); flex: none; }
  .brand--front { left: 70px; top: 90px; color: var(--white); font-size: 66px; }
  .brand--front .brand__mark { width: 40px; height: 40px; }
  .brand--back { left: 22px; top: 128px; color: var(--ink); font-size: 33px; gap: 8px; }
  .brand--back .brand__mark { width: 20px; height: 20px; }

  .website {
    position: absolute; left: 0; right: 0; top: 282px;
    text-align: center; color: var(--white); font-size: 19px;
  }

  .contact-panel {
    position: absolute; left: 290px; top: 0; width: 291px; height: 329px;
    background: var(--navy); color: var(--white);
  }
  .contact-panel__name {
    position: absolute; left: 24px; top: 62px; font-size: 33px; font-weight: 700;
  }
  .contact-panel__role {
    position: absolute; left: 24px; top: 102px; font-size: 25px; color: var(--green);
  }
  .contact-panel__address {
    position: absolute; left: 24px; top: 176px; font-size: 14px; line-height: 1.45;
    font-style: normal;
  }
  .contact-panel__lines {
    position: absolute; left: 24px; top: 233px; width: 245px; font-size: 14px;
    list-style: none; line-height: 1.4;
  }
  .contact-panel__lines li { display: flex; }
  .contact-panel__lines .label { color: var(--green); width: 110px; }
  .contact-panel__email {
    position: absolute; right: 22px; top: 289px; font-size: 14px;
  }
</style>
</head>
<body>
<main class="stage">
  <section class="card card--front" aria-label="Business card front">
    <div class="brand brand--front"><span class="brand__mark"></span>Velin Medical</div>
    <p class="website">www.velinmedical.net</p>
  </section>

  <section class="card card--back" aria-label="Business card back">
    <div class="brand brand--back"><span class="brand__mark"></span>Velin Medical</div>
    <div class="contact-panel">
      <h1 class="contact-panel__name">Tobias Morvel</h1>
      <p class="contact-panel__role">CEO</p>
      <address class="contact-panel__address">12345 Any Street,<br>Lindmere, CA 98765</address>
      <ul class="contact-panel__lines">
        <li><span class="label">p:</span>(123) 456 7890</li>
        <li><span class="label">f:</span>(123) 456 7890</li>
        <li><span class="label">c:</span>(123) 456 7890</li>
      </ul>
      <p class="contact-panel__email">tmorvel@velinmedical.net</p>
    </div>
  </section>
</main>
</body>
</html>
```